Engineering and Energy service provider

We need a design that gives the impression of a high level of technical competence and a reliable partner. Simple structure with little need for updates.
The company brand is Vornik and today consists of two main businesses: energy optimisation (Vornik energy) and technical consultancy (Vornik Engineering). Vornik energy is shown in the attached powerpoint,
We are a young growing company that consists of several businesses, the largest parts are energy monitoring services and consulting services. Consulting services for commercial installations in the technical area of cooling, ventilation, heating and energy. Services offered include project planning, project management, inspection, operational analysis and technical investigations. Energy monitoring and optimization services are performed as a subscription with a subscription to the service.
Target Market(s)
Commercial property owners Grocery retail, grocery stores, construction companies
Industry/Entity Type
energy services and consulting services
Coding
Coded - Design and coding required
Number of Pages Required
5+ page
Look and feel

```html
<!DOCTYPE html>
<html lang="en">
<head>
<meta charset="utf-8">
<title>Vornik – Energy Optimisation and Technical Consulting</title>
<link href="https://fonts.googleapis.com/css2?family=Inter:wght@400;500;600;700&family=Poppins:ital,wght@0,600;0,700;1,700;1,800&display=swap" rel="stylesheet">
<style>
:root{
  --blue:#1658b8;
  --blue-deep:#0f4aa3;
  --navy:#0b1b4a;
  --footer:#0a1a3f;
  --panel:#f1f3f6;
  --text:#333b4a;
  --muted:#6b7280;
  --white:#ffffff;
}
*{margin:0;padding:0;box-sizing:border-box}
html,body{width:1200px;height:3736px;overflow:hidden}
body{position:relative;background:var(--white);font-family:"Inter",sans-serif;color:var(--text)}
.abs{position:absolute}
.heading{font-family:"Poppins",sans-serif;font-style:italic;font-weight:800}
.btn{position:absolute;display:flex;align-items:center;justify-content:center;font-family:"Inter",sans-serif;font-weight:700;font-size:11.5px;letter-spacing:.3px;text-transform:uppercase;clip-path:polygon(0 0,92% 0,100% 100%,0 100%)}
.btn.blue{background:var(--blue);color:var(--white);clip-path:polygon(6% 0,100% 0,94% 100%,0 100%)}
.btn.white{background:var(--white);color:var(--navy)}
.wordmark{font-family:"Poppins",sans-serif;font-weight:700;letter-spacing:4px;color:var(--white)}
.ph{position:absolute}

/* hero */
.hero{position:absolute;left:0;top:0;width:1200px;height:607px;background:linear-gradient(135deg,#1a5fc2,#1350aa);overflow:hidden}
.hero-photo{left:0;top:0;width:1200px;height:607px;clip-path:polygon(435px 0,1200px 0,1200px 607px,762px 607px);background:linear-gradient(180deg,#6b7f9a 0%,#d9a45a 45%,#e8a048 55%,#4d5a3a 80%,#3a4230 100%)}
.hero-band{left:0;top:0;width:1200px;height:607px;background:rgba(255,255,255,.85);clip-path:polygon(428px 0,435px 0,762px 607px,755px 607px)}
.side-name{position:absolute;font-family:"Poppins",sans-serif;font-weight:700;color:rgba(255,255,255,.12);letter-spacing:6px;transform-origin:left top;transform:rotate(90deg);white-space:nowrap}
.nav{position:absolute;top:19px;left:499px;display:flex;height:36px;align-items:center}
.nav a{color:var(--white);text-decoration:none;font-size:11px;font-weight:500;margin-right:28px}
.hero h1{position:absolute;left:120px;top:166px;color:var(--white);font-size:43px;line-height:57px;white-space:nowrap}
.hero p{position:absolute;left:124px;top:400px;width:480px;color:var(--white);font-size:12px;line-height:17px;font-style:italic}

/* section titles */
.sec-title{position:absolute;left:0;width:1200px;text-align:center;font-size:36px;color:var(--navy)}
.sec-title span{color:var(--blue)}
.sec-title .bars{display:inline-block;vertical-align:middle;width:17px;height:14px;margin:0 6px;background:linear-gradient(var(--navy) 0 2px,transparent 2px 6px,var(--navy) 6px 8px,transparent 8px 12px,var(--navy) 12px 14px)}

/* services */
.svc-panel{position:absolute;background:var(--panel)}
.svc-title{position:absolute;font-size:26px;color:var(--navy)}
.svc-sub{position:absolute;font-size:11px;color:var(--text)}
.svc-list{position:absolute;list-style:none}
.svc-list li{font-size:13.5px;font-weight:500;color:var(--blue);height:32px;padding-left:19px;position:relative}
.svc-list li::before{content:"";position:absolute;left:0;top:3px;border-left:9px solid var(--blue);border-top:6px solid transparent;border-bottom:6px solid transparent}

/* about */
.about-text{position:absolute;left:707px;width:340px;color:var(--white);font-size:11px;line-height:15px}

/* why */
.why-item{position:absolute;width:200px;text-align:center;top:1954px}
.why-item svg{display:block;margin:0 auto}
.why-item p{margin-top:10px;font-size:14px;font-weight:600;color:var(--navy);line-height:19px}

/* blog */
.card{position:absolute;top:2648px;width:306px;height:320px;border-bottom:1px solid #d7dbe2}
.card .img{position:absolute;left:0;top:0;width:306px;height:202px}
.card .date{position:absolute;left:0;top:184px;background:var(--blue);color:var(--white);font-size:9px;padding:3px 10px}
.card h3{position:absolute;left:0;top:224px;font-size:14.5px;font-weight:600;color:var(--navy);line-height:19px}
.card p{position:absolute;left:0;top:266px;width:220px;font-size:10.5px;color:var(--muted);line-height:14px}
.card svg{position:absolute;right:0;top:296px}

/* cta */
.cta h2{position:absolute;left:718px;top:3178px;color:var(--white);font-size:34px;line-height:44px;white-space:nowrap}
.cta p{position:absolute;left:718px;top:3322px;width:310px;color:var(--white);font-size:11px;line-height:15px}

/* footer */
.footer{position:absolute;left:0;top:3494px;width:1200px;height:242px;background:var(--footer);color:var(--white)}
.f-head{position:absolute;top:38px;font-family:"Poppins",sans-serif;font-style:italic;font-weight:700;font-size:14px}
.f-list{position:absolute;list-style:none;font-size:10px}
.f-list li{display:flex;align-items:center;gap:8px}
.f-div{position:absolute;top:28px;width:1px;height:170px;background:rgba(255,255,255,.2)}
.dot{width:18px;height:18px;border:1.3px solid var(--white);border-radius:50%;flex:none}
</style>
</head>
<body>

<!-- HERO -->
<section class="hero">
  <div class="ph hero-photo" role="img" aria-label="Engineer in hard hat and safety vest holding a tablet in front of wind turbines at sunset"></div>
  <div class="ph hero-band"></div>
  <div class="side-name" style="left:78px;top:165px;font-size:72px">VORNIK</div>
  <div class="abs wordmark" style="left:122px;top:16px;font-size:30px">VORNIK</div>
  <nav class="nav">
    <a href="#">ABOUT</a><a href="#">VORNIK ENERGY</a><a href="#">VORNIK ENGINEERING</a><a href="#">PROJECT</a><a href="#">BLOG</a>
  </nav>
  <div class="btn blue" style="left:953px;top:19px;width:124px;height:36px">Contact Us</div>
  <h1 class="heading">Your Reliable<br>Partner in Energy<br>Optimisation and<br>Technical Consulting</h1>
  <p>At Vornik, we combine advanced technical expertise with smart energy solutions to create efficient, sustainable, and cost-effective systems for commercial installations</p>
  <div class="btn white" style="left:126px;top:464px;width:200px;height:41px">Explore Our Services</div>
</section>

<!-- SERVICES -->
<h2 class="sec-title heading" style="top:656px"><i class="bars"></i>Our <span>Services</span><i class="bars"></i></h2>

<div class="ph" role="img" aria-label="Electricity pylons against a sunset sky" style="left:122px;top:727px;width:471px;height:308px;background:linear-gradient(180deg,#1f4fa8 0%,#7d8fb0 45%,#f0b040 70%,#6b4a1a 100%)"></div>
<div class="abs" style="left:593px;top:727px;width:12px;height:617px;background:var(--blue)"></div>
<div class="svc-panel" style="left:605px;top:727px;width:475px;height:308px"></div>
<div class="abs" style="left:605px;top:873px;border-left:10px solid var(--blue);border-top:8px solid transparent;border-bottom:8px solid transparent"></div>
<svg class="abs" style="left:676px;top:765px" width="74" height="66" viewBox="0 0 74 66"><polygon points="18,2 56,2 72,33 56,64 18,64 2,33" fill="none" stroke="#1658b8" stroke-width="2.5"/><polygon points="22,9 52,9 64,33 52,57 22,57 10,33" fill="#1658b8"/><circle cx="37" cy="33" r="11" fill="none" stroke="#fff" stroke-width="2.5"/><path d="M38 25l-5 9h5l-2 8 6-10h-5z" fill="#fff"/></svg>
<h3 class="svc-title heading" style="left:768px;top:766px">Vornik Energy</h3>
<div class="svc-sub" style="left:768px;top:804px">Vornik Energy – Smarter Energy Management</div>
<ul class="svc-list" style="left:766px;top:832px"><li>Energy Audits</li><li>Building Optimization</li><li>Renewable Integration</li></ul>
<div class="btn blue" style="left:701px;top:948px;width:265px;height:42px">Learn More Vornik Energy</div>

<div class="svc-panel" style="left:122px;top:1035px;width:471px;height:309px"></div>
<div class="abs" style="left:583px;top:1182px;border-right:10px solid var(--blue);border-top:8px solid transparent;border-bottom:8px solid transparent"></div>
<svg class="abs" style="left:170px;top:1078px" width="74" height="66" viewBox="0 0 74 66"><polygon points="18,2 56,2 72,33 56,64 18,64 2,33" fill="none" stroke="#1658b8" stroke-width="2.5"/><polygon points="22,9 52,9 64,33 52,57 22,57 10,33" fill="#1658b8"/><circle cx="37" cy="33" r="10" fill="none" stroke="#fff" stroke-width="3" stroke-dasharray="4 3"/><circle cx="37" cy="33" r="4" fill="#fff"/></svg>
<h3 class="svc-title heading" style="left:263px;top:1082px">Vornik Engineering</h3>
<div class="svc-sub" style="left:263px;top:1120px">Vornik Engineering – Precision. Innovation. Reliability</div>
<ul class="svc-list" style="left:260px;top:1149px"><li>Mechanical &amp; Electrical Engineering</li><li>Project Design &amp; Supervision</li><li>Technical Due Diligence</li></ul>
<div class="btn blue" style="left:196px;top:1264px;width:265px;height:43px">Learn More Vornik Engineering</div>
<div class="ph" role="img" aria-label="Engineer in a hard hat checking an electrical cabinet with a tablet" style="left:605px;top:1035px;width:475px;height:309px;background:linear-gradient(120deg,#c9ccd0 0%,#8a8f96 45%,#3c4149 75%,#5a6069 100%)"></div>

<!-- ABOUT -->
<div class="abs" style="left:0;top:1407px;width:120px;height:410px;background:linear-gradient(160deg,#1e63c4,#1350aa)"></div>
<div class="ph" role="img" aria-label="Two engineers in safety vests walking past a wind turbine and solar panels" style="left:132px;top:1407px;width:435px;height:410px;background:linear-gradient(180deg,#b9c8d6 0%,#dde5ec 45%,#6f8a4e 75%,#4f6a36 100%)"></div>
<div class="abs" style="left:579px;top:1407px;width:621px;height:410px;background:linear-gradient(150deg,#1e63c4,#1350aa);clip-path:polygon(0 0,510px 0,545px 35px,621px 35px,621px 410px,0 410px)"></div>
<div class="side-name" style="left:1200px;top:1440px;font-size:72px;color:rgba(255,255,255,.14)">VORNIK</div>
<h2 class="abs heading" style="left:707px;top:1486px;font-size:35px;color:var(--white)">About Vornik <i style="display:inline-block;vertical-align:middle;width:17px;height:14px;background:linear-gradient(#fff 0 2px,transparent 2px 6px,#fff 6px 8px,transparent 8px 12px,#fff 12px 14px)"></i></h2>
<p class="about-text" style="top:1541px">Vornik is a growing, technology-driven company specialising in energy optimisation and technical consultancy. We deliver reliable data-backed solutions that improve energy performance and operational efficiency across complex technical systems.</p>
<p class="about-text" style="top:1608px">Our experienced team provides deep knowledge in cooling, ventilation, heating, and energy systems ensuring precision, sustainability, and measurable results.</p>
<div class="btn white" style="left:707px;top:1682px;width:145px;height:42px">Learn More</div>

<!-- WHY CHOOSE US -->
<h2 class="sec-title heading" style="top:1862px"><i class="bars"></i>Why<span>Choose Us</span><i class="bars"></i></h2>
<div class="why-item" style="left:89px"><svg width="94" height="82" viewBox="0 0 94 82"><polygon points="23,2 71,2 92,41 71,80 23,80 2,41" fill="none" stroke="#1658b8" stroke-width="2.5"/><polygon points="28,10 66,10 82,41 66,72 28,72 12,41" fill="#fff" stroke="#1658b8" stroke-width="2"/><rect x="32" y="32" width="30" height="20" rx="3" fill="#1658b8"/><rect x="41" y="27" width="12" height="6" rx="1" fill="none" stroke="#1658b8" stroke-width="2"/></svg><p>Proven<br>Technical Expertise</p></div>
<div class="why-item" style="left:361px"><svg width="94" height="82" viewBox="0 0 94 82"><polygon points="23,2 71,2 92,41 71,80 23,80 2,41" fill="none" stroke="#1658b8" stroke-width="2.5"/><polygon points="28,10 66,10 82,41 66,72 28,72 12,41" fill="#fff" stroke="#1658b8" stroke-width="2"/><circle cx="47" cy="34" r="8" fill="#1658b8"/><path d="M32 55c2-9 8-12 15-12s13 3 15 12z" fill="#1658b8"/></svg><p>Independent<br>Consultancy</p></div>
<div class="why-item" style="left:636px"><svg width="94" height="82" viewBox="0 0 94 82"><polygon points="23,2 71,2 92,41 71,80 23,80 2,41" fill="none" stroke="#1658b8" stroke-width="2.5"/><polygon points="28,10 66,10 82,41 66,72 28,72 12,41" fill="#fff" stroke="#1658b8" stroke-width="2"/><path d="M28 42l10-8 9 4 9-4 10 8-12 12-7-6-7 6z" fill="#1658b8"/></svg><p>Reliable Long<br>Term Partner</p></div>
<div class="why-item" style="left:908px"><svg width="94" height="82" viewBox="0 0 94 82"><polygon points="23,2 71,2 92,41 71,80 23,80 2,41" fill="none" stroke="#1658b8" stroke-width="2.5"/><polygon points="28,10 66,10 82,41 66,72 28,72 12,41" fill="#fff" stroke="#1658b8" stroke-width="2"/><rect x="36" y="27" width="22" height="28" rx="2" fill="#1658b8"/><path d="M41 41l4 4 8-8" stroke="#fff" stroke-width="2.5" fill="none"/></svg><p>Focus on<br>Sustainable Results</p></div>

<!-- PROJECT GALLERY -->
<h2 class="sec-title heading" style="top:2134px"><i class="bars"></i>Our Project <span>Gallery</span><i class="bars"></i></h2>
<div class="ph" role="img" aria-label="Row of wind turbines with an engineer, in black and white" style="left:0;top:2200px;width:355px;height:297px;background:linear-gradient(180deg,#f2f2f2 0%,#cfcfcf 60%,#6e6e6e 100%)"></div>
<div class="ph" role="img" aria-label="Electricity pylon under a cloudy evening sky" style="left:361px;top:2200px;width:478px;height:297px;border:3px solid var(--blue);background:linear-gradient(180deg,#7d8ea3 0%,#b9b9a4 50%,#c8a65e 75%,#5a5436 100%)"></div>
<div class="ph" role="img" aria-label="Engineer using a tablet at an electrical cabinet, in black and white" style="left:846px;top:2200px;width:354px;height:297px;background:linear-gradient(120deg,#9a9a9a 0%,#5c5c5c 50%,#c4c4c4 100%)"></div>
<svg class="abs" style="left:571px;top:2518px" width="58" height="26" viewBox="0 0 58 26"><circle cx="13" cy="13" r="11.5" fill="none" stroke="#0b1b4a" stroke-width="1.3"/><path d="M18 13H8m4-4l-4 4 4 4" stroke="#0b1b4a" stroke-width="1.5" fill="none"/><circle cx="45" cy="13" r="11.5" fill="none" stroke="#0b1b4a" stroke-width="1.3"/><path d="M40 13h10m-4-4l4 4-4 4" stroke="#0b1b4a" stroke-width="1.5" fill="none"/></svg>

<!-- LATEST BLOG -->
<h2 class="sec-title heading" style="top:2578px"><i class="bars"></i>Latest Blog<i class="bars"></i></h2>
<article class="card" style="left:122px">
  <div class="img" role="img" aria-label="Person working on a laptop beside a model wind turbine" style="background:linear-gradient(135deg,#e4e7ea,#8c939b 60%,#3c4048)"></div>
  <span class="date">8. Sep 2025</span>
  <h3>The Importance of<br>Energy Monitoring</h3>
  <p>Monitoring energy usage in real time gives building operators the data they need to make informed decisio.</p>
  <svg width="16" height="16" viewBox="0 0 16 16"><path d="M3 13L13 3M5 3h8v8" stroke="#1658b8" stroke-width="1.5" fill="none"/></svg>
</article>
<article class="card" style="left:447px">
  <div class="img" role="img" aria-label="Two engineers reviewing a laptop in a server room" style="background:linear-gradient(135deg,#2c3440,#5b6673 55%,#cfd6dd)"></div>
  <span class="date">8. Sep 2025</span>
  <h3>Technical Consulting for<br>Optimised Operations</h3>
  <p>Monitoring energy usage in real time gives building operators the data they need to make informed decisio.</p>
  <svg width="16" height="16" viewBox="0 0 16 16"><path d="M3 13L13 3M5 3h8v8" stroke="#1658b8" stroke-width="1.5" fill="none"/></svg>
</article>
<article class="card" style="left:772px">
  <div class="img" role="img" aria-label="Woman with a VR headset beside small green wind turbine models" style="background:linear-gradient(135deg,#f3f4f5,#d8dbdf 55%,#a9b0b8)"></div>
  <span class="date">8. Sep 2025</span>
  <h3>Subscription-Based<br>Energy Optimisation</h3>
  <p>Monitoring energy usage in real time gives building operators the data they need to make informed decisio.</p>
  <svg width="16" height="16" viewBox="0 0 16 16"><path d="M3 13L13 3M5 3h8v8" stroke="#1658b8" stroke-width="1.5" fill="none"/></svg>
</article>
<div class="btn blue" style="left:521px;top:3000px;width:158px;height:41px">View All Blog</div>

<!-- CTA -->
<section class="cta">
  <div class="ph" role="img" aria-label="Two engineers in hard hats reviewing plans on a tablet" style="left:0;top:3107px;width:1200px;height:387px;background:linear-gradient(90deg,#6d747c,#a7adb3 50%,#4d535b);clip-path:polygon(0 0,741px 0,434px 387px,0 387px)"></div>
  <div class="abs" style="left:0;top:3107px;width:1200px;height:387px;background:rgba(255,255,255,.9);clip-path:polygon(741px 0,748px 0,441px 387px,434px 387px)"></div>
  <div class="abs" style="left:0;top:3107px;width:1200px;height:387px;background:linear-gradient(150deg,#1e63c4,#1350aa);clip-path:polygon(748px 0,1105px 0,1130px 20px,1200px 20px,1200px 387px,441px 387px)"></div>
  <div class="side-name" style="left:1200px;top:3140px;font-size:72px;color:rgba(255,255,255,.14)">VORNIK</div>
  <h2 class="heading">Let’s Create Smarter<br>More Efficient<br>Systems Together</h2>
  <p>Whether you need ongoing energy optimisation or expert consulting support, Vornik is here to help you achieve measurable performance improvements.</p>
  <div class="btn white" style="left:718px;top:3390px;width:160px;height:41px">Contact Us</div>
</section>

<!-- FOOTER -->
<footer class="footer">
  <div class="abs wordmark" style="left:122px;top:34px;font-size:26px">VORNIK</div>
  <p class="abs" style="left:122px;top:84px;width:185px;font-size:9.5px;line-height:14px">Vornik is a growing, technology-driven company specialising in energy optimisation and technical consultancy.</p>
  <div class="abs" style="left:122px;top:136px;width:30px;height:30px;background:var(--white)"></div>
  <p class="abs" style="left:160px;top:140px;font-size:9px;line-height:11px">Certified<br>Solvane Partner</p>
  <div class="f-div" style="left:321px"></div>

  <h4 class="f-head" style="left:368px">Contact Us</h4>
  <ul class="f-list" style="left:366px;top:62px">
    <li style="height:30px"><span class="dot"></span><span style="color:#3d7be0">info@vornik-group.example</span></li>
    <li><span class="dot"></span>+49 (6200) 4471</li>
  </ul>
  <div class="f-div" style="left:540px"></div>

  <h4 class="f-head" style="left:560px">Main Link</h4>
  <ul class="f-list" style="left:560px;top:66px;line-height:21.5px;display:block">
    <li>Home</li><li>About</li><li>Vornik Energy</li><li>Vornik Engineering</li><li>Contact Us</li>
  </ul>
  <div class="f-div" style="left:690px"></div>

  <h4 class="f-head" style="left:744px">Service Areas</h4>
  <ul class="f-list" style="left:742px;top:62px">
    <li style="height:30px"><span class="dot"></span>Friendwall</li>
    <li style="height:30px"><span class="dot"></span>Workline</li>
    <li style="height:30px"><span class="dot"></span>Vidstream</li>
    <li style="height:30px"><span class="dot"></span>Snapgram</li>
  </ul>
  <div class="f-div" style="left:872px"></div>

  <h4 class="f-head" style="left:908px">Subscribe Newsletter</h4>
  <div class="abs" style="left:908px;top:67px;width:170px;height:37px;border:1px solid rgba(255,255,255,.7);font-size:10px;padding:12px 13px">Enter Your Email</div>
  <div class="btn blue" style="left:908px;top:122px;width:156px;height:40px">Subscribe</div>

  <div class="abs" style="left:113px;top:205px;width:975px;height:1px;background:rgba(255,255,255,.25)"></div>
  <p class="abs" style="left:0;top:219px;width:1200px;text-align:center;font-size:9px">© Copyright Vornik 2025 | Legal Notice | Legal information | Data Privacy</p>
</footer>

</body>
</html>
```